Electrical contractor

looking for a standard sized, horizontal, double sided business card for an electrical contractors business.
i have played around on microsoft word (only computer program i know how to use!) and will attach what i have made so far, really open to any ideas. i just want the DORB to stand out to the rest of the business name.

i wish to use the colours black and green, and white for writing. i will attach the pictures i took off google, i want to either use them, or somethin similar for the back grounds

i wish the front to have the following info:
business name: D.O.R.B ELECTRICAL CONTRACTORS
MY NAME; CORBIN HOLT
STATUS; A CLASS ELECTRICIAN
LICENSE NO; TRN517394
PH NO. 0431576204
EMAIL ADD. DORB.ELECTRICAL@VELTOMAIL.COM
AND MY SLOGAN: where excellence meets integrity, and service comes with a smile.

i am not sure what to have on the back, other than what i do for work.eg titled WHAT WE DO
i dont want too much written on there or will look crowded, but options to add to back, from most important to least, please pick however many you think will look the best
new homes/extentions
led lighting and downlights
Solar Power
power
safety switches
switchboards
telephone and tv
smoke alarms
stoves and ovens
hot water systems
fault finding
re wiring
Updates

Thank you to those who have submitted designs, I would like to change my slogan to something more simple, I'm thinking something like. RELIABLE. EFFICIENT. PROFESSIONAL. AFFORDABLE. in what ever order you thinks fits best. Thanks

Industry/Entity Type

Contractor

```html
<!DOCTYPE html>
<html lang="en">
<head>
<meta charset="utf-8">
<title>D.O.R.B Electrical Contractors – Business Card</title>
<link rel="stylesheet" href="https://fonts.googleapis.com/css2?family=Open+Sans:wght@400;600&display=swap">
<style>
  :root {
    --canvas-bg: #e9e9e9;
    --ink-white: #ffffff;
    --ink-soft: #cfd8e6;
    --back-black: #050607;
    --back-charcoal: #111418;
    --service-green: #1f5a3e;
    --front-navy: #0b2344;
    --front-blue: #1b4f8a;
    --spark-blue: #4fa9e6;
    --glow-magenta: #b23a78;
  }
  * { margin: 0; padding: 0; box-sizing: border-box; }
  html, body {
    width: 1200px; height: 1050px; overflow: hidden;
    background: var(--canvas-bg);
    font-family: "Open Sans", sans-serif;
    color: var(--ink-white);
  }
  .canvas { position: relative; width: 1200px; height: 1050px; }
  .card {
    position: absolute; left: 180px; width: 840px; height: 480px;
    overflow: hidden; box-shadow: 0 6px 18px rgba(0,0,0,.25);
  }

  /* Back of card */
  .card-back {
    top: 30px;
    background: linear-gradient(160deg, var(--back-charcoal) 0%, var(--back-black) 60%);
  }
  .back-glow {
    position: absolute; left: 420px; top: 230px; width: 420px; height: 250px;
    background: radial-gradient(ellipse 40% 35% at 45% 55%, rgba(255,220,235,.9) 0%, rgba(178,58,120,.55) 25%, rgba(60,20,60,.35) 55%, rgba(0,0,0,0) 80%);
  }
  .back-wordmark {
    position: absolute; left: 320px; top: 26px;
    font-size: 58px; font-weight: 400; letter-spacing: 6px; line-height: 1;
  }
  .back-slogan {
    position: absolute; left: 150px; top: 100px;
    font-size: 19px; font-weight: 400;
  }
  .services-title {
    position: absolute; left: 40px; top: 140px; width: 250px;
    font-size: 20px; padding-bottom: 6px;
    border-bottom: 1px solid var(--ink-white);
  }
  .services-list { list-style: none; position: absolute; left: 0; top: 190px; }
  .service-item {
    display: block; height: 40px; margin-bottom: 10px;
    padding: 6px 0 0 40px;
    background: var(--service-green);
    border: 1px solid rgba(255,255,255,.35); border-left: none;
    font-size: 19px;
  }
  .service-item:nth-child(1) { width: 330px; }
  .service-item:nth-child(2) { width: 350px; }
  .service-item:nth-child(3) { width: 330px; }
  .service-item:nth-child(4) { width: 230px; }

  /* Front of card */
  .card-front {
    top: 540px;
    background: linear-gradient(170deg, var(--front-navy) 0%, var(--front-blue) 100%);
  }
  .front-spark {
    position: absolute; left: 430px; top: 240px; width: 410px; height: 240px;
    background: radial-gradient(ellipse 45% 30% at 50% 55%, rgba(255,255,255,.85) 0%, rgba(79,169,230,.6) 30%, rgba(27,79,138,0) 75%);
  }
  .front-brand { position: absolute; left: 0; top: 40px; width: 840px; text-align: center; }
  .front-wordmark { font-size: 92px; font-weight: 400; letter-spacing: 10px; line-height: 1; }
  .front-tagline { margin-top: 10px; font-size: 21px; letter-spacing: 1px; }
  .holder { position: absolute; left: 50px; top: 215px; }
  .holder-name { font-size: 44px; font-weight: 400; line-height: 1.1; }
  .holder-status {
    font-size: 18px; width: 330px; padding: 6px 0 8px 12px;
    border-bottom: 1px solid var(--ink-white);
  }
  .contact { list-style: none; margin-top: 12px; padding-left: 12px; }
  .contact li { font-size: 20px; line-height: 1.35; color: var(--ink-soft); }
</style>
</head>
<body>
<main class="canvas">

  <section class="card card-back" aria-label="Back of business card">
    <div class="back-glow" role="img" aria-label="Glowing light bulb on a dark background"></div>
    <div class="back-wordmark">D.O.R.B</div>
    <p class="back-slogan">where excellence meets integrity, and service comes with a smile</p>
    <h2 class="services-title">Our services :</h2>
    <ul class="services-list">
      <li class="service-item">Led lighting and downlights</li>
      <li class="service-item">Telephone and tv</li>
      <li class="service-item">New homes/extentions</li>
      <li class="service-item">Many others...</li>
    </ul>
  </section>

  <section class="card card-front" aria-label="Front of business card">
    <div class="front-spark" role="img" aria-label="Electric spark arcing between two stripped copper wires"></div>
    <header class="front-brand">
      <div class="front-wordmark">D.O.R.B</div>
      <p class="front-tagline">ELECTRICAL CONTRACTORS</p>
    </header>
    <div class="holder">
      <h1 class="holder-name">CORBIN HOLT</h1>
      <p class="holder-status">A CLASS ELECTRICIAN</p>
      <ul class="contact">
        <li>PH NO. 0431576204</li>
        <li>LICENSE NO; TRN517394</li>
        <li>DORB.ELECTRICAL@VELTOMAIL.COM</li>
      </ul>
    </div>
  </section>

</main>
</body>
</html>
```